New Alcoholic Spiked Seltzer Line

We need a can design for a line of low calorie alcoholic seltzer. This product is a sparkling water and vodka drink with no sugar added in a slim 12 oz can.

This is a lighter, healthier, alternative to the sugary ready-to-drinks on the market. The product contains only 3 ingredients: Vodka, Water and Natural Flavors. It has only 100 calories but still has 5% alcohol, so you don't need to sacrifice alcohol to cut calories.

This product also does not contain any preservatives.

We want this design to communicate the following objectives to the consumer and in this order:

1. Appetizing product
2.Low calorie
3.Communicate the type of beverage (Spiked Seltzer)

The brand name of the product is VELKA.

The flavor of the product needed to be used for the design is Mango-Orange.

Comparable products are:

www.brisavelfizz.example/
https://www.tarnowbubble.example
https://quellrind.example/

The designs should not infringe or copy the creative directions of the products mentionned above. They are only given so that you can better understand the type of product we are developing.

Target Market(s)

Young Professional women between the ages of 25 and 44

Industry/Entity Type

Product

Colors

Designer to choose colors to be used in the design.

Requirements
Must have
• Design extendibility, meaning it can be adapted for other flavors.
• This is a new category in the market we are targeting, so consumers must easily be able to identify what type of product this is.

```html
<!DOCTYPE html>
<html lang="en">
<head>
<meta charset="utf-8">
<title>VELKA Mango Orange Spiked Seltzer</title>
<link rel="stylesheet" href="https://fonts.googleapis.com/css2?family=Oswald:wght@500;600&display=swap">
<style>
  :root {
    --citrus-light: #ffc23a;
    --citrus-mid: #f59a12;
    --citrus-deep: #e07a05;
    --night: #0d0d0d;
    --night-soft: #2a2a2a;
    --brand-white: #ffffff;
    --flavor-yellow: #f7b516;
  }
  html, body {
    margin: 0;
    padding: 0;
    overflow: hidden;
    background: var(--night);
  }
  .can-label {
    position: relative;
    width: 837px;
    height: 1200px;
    overflow: hidden;
    background: var(--night);
  }
  .fruit-photo {
    position: absolute;
    inset: 0;
    background: radial-gradient(ellipse at 25% 10%, var(--citrus-light) 0%, var(--citrus-mid) 45%, var(--citrus-deep) 100%);
  }
  .stripe-panel {
    position: absolute;
    inset: 0;
    width: 837px;
    height: 1200px;
  }
  .brand-name {
    position: absolute;
    left: 444px;
    top: 105px;
    transform: translateX(-50%);
    margin: 0;
    display: flex;
    flex-direction: column;
    align-items: center;
    font-family: "Oswald", sans-serif;
    font-weight: 500;
    font-size: 184px;
    line-height: 192px;
    color: var(--brand-white);
  }
  .product-info {
    position: absolute;
    left: 397px;
    top: 1098px;
    transform: translateX(-50%);
    text-align: center;
    font-family: "Oswald", sans-serif;
    font-weight: 600;
    font-size: 29px;
    line-height: 35px;
    letter-spacing: 0.5px;
    white-space: nowrap;
  }
  .flavor { color: var(--flavor-yellow); margin: 0; }
  .category { color: var(--brand-white); margin: 0; }
</style>
</head>
<body>
  <main class="can-label">
    <div class="fruit-photo" role="img" aria-label="Photo of freshly sliced oranges"></div>
    <svg class="stripe-panel" viewBox="0 0 837 1200" role="img" aria-label="Black panel with diagonal stripe pattern">
      <defs>
        <linearGradient id="panelShade" x1="0" y1="0" x2="1" y2="1">
          <stop offset="0" stop-color="#222"/>
          <stop offset="0.5" stop-color="#151515"/>
          <stop offset="1" stop-color="#1f1f1f"/>
        </linearGradient>
      </defs>
      <path d="M0,352 Q300,20 812,0 L837,0 L837,1200 L0,1200 Z" fill="url(#panelShade)"/>
    </svg>
    <h1 class="brand-name" aria-label="VELKA">
      <span>V</span><span>E</span><span>L</span><span>K</span><span>A</span>
    </h1>
    <div class="product-info">
      <p class="flavor">MANGO ORANGE</p>
      <p class="category">SPIKED SELTZER</p>
    </div>
  </main>
</body>
</html>
```